What happens?

Develop a graphic to be used on a church web page based on the following:

"What happens at the intersection of spirituality, sexuality and social justice?"
A second graphic will use the first concept and add an answer to it. "healing, creativity, acceptance, forgiveness, wholeness, service, freedom."

The graphic should be shades of gray, possibly with touches of color (yellow and blue).
This design needs to convey the idea of intersection not just be text.

Attached is a very rough graphic concept to use as a starting point.

Target Market(s)

young adults interested in progressive spirituality rather than dogmatic religion

Industry/Entity Type

Church

Font styles to use
Sans Serif

Requirements
Must have
• visual concept of intersection, visually tying of the answers to the question
Should not have
• just text

```html
<!DOCTYPE html>
<html lang="en">
<head>
<meta charset="utf-8">
<title>What Happens at the Intersection?</title>
<link rel="stylesheet" href="https://fonts.googleapis.com/css2?family=Cinzel:wght@400&family=Oswald:wght@600&family=Permanent+Marker&family=Rubik:wght@700&display=swap">
<style>
  :root {
    --page-bg: #d9d9d9;
    --card-bg: #f2f2f2;
    --ink-black: #111111;
    --ink-grey: #6b6b6b;
    --ink-grey-dark: #4a4a4a;
    --rule: #c4c4c4;
    --yellow: #ffd21a;
    --yellow-deep: #d9a400;
    --yellow-light: #fff3a6;
    --purple: #d23cf0;
    --purple-deep: #7a1f9e;
    --purple-light: #f3c2ff;
    --blue: #3d8cff;
    --blue-deep: #1a4fc0;
    --blue-light: #cfe3ff;
  }
  html, body {
    margin: 0;
    width: 1200px;
    height: 820px;
    overflow: hidden;
    background: var(--page-bg);
  }
  .canvas {
    width: 1200px;
    height: 820px;
    display: flex;
    align-items: center;
    justify-content: center;
  }
  .poster {
    width: 984px;
    height: 816px;
    background: var(--card-bg);
    box-shadow: 0 2px 10px rgba(0,0,0,.18);
  }
  .poster svg { display: block; width: 100%; height: 100%; }
  .title-what { font-family: "Permanent Marker", cursive; font-size: 64px; fill: var(--ink-black); }
  .title-happens { font-family: "Cinzel", serif; font-size: 40px; fill: var(--ink-grey); }
  .title-intersection { font-family: "Oswald", sans-serif; font-weight: 600; font-size: 56px; }
  .tile-letter { font-family: "Rubik", sans-serif; font-weight: 700; font-size: 17px; text-anchor: middle; }
  .tile-yellow rect { fill: var(--yellow-deep); opacity: .75; }
  .tile-yellow text { fill: var(--yellow-light); }
  .tile-purple rect { fill: var(--purple-deep); opacity: .85; }
  .tile-purple text { fill: var(--purple-light); }
  .tile-blue rect { fill: var(--blue-deep); opacity: .9; }
  .tile-blue text { fill: var(--blue-light); }
  .question-mark { font-family: "Oswald", sans-serif; font-weight: 600; font-size: 22px; fill: #8a8a8a; text-anchor: middle; }
</style>
</head>
<body>
<main class="canvas">
  <section class="poster" aria-label="What happens at the intersection of spirituality, sexuality and social justice?">
    <svg viewBox="0 0 568 472" xmlns="http://www.w3.org/2000/svg">
      <defs>
        <linearGradient id="title-fill" x1="0" y1="0" x2="0" y2="1">
          <stop offset="0" stop-color="#8c8c8c"/>
          <stop offset="1" stop-color="#3f3f3f"/>
        </linearGradient>
        <radialGradient id="burst" cx="285" cy="297" r="300" gradientUnits="userSpaceOnUse">
          <stop offset="0" stop-color="#ffffff"/>
          <stop offset=".6" stop-color="#f4f4f4"/>
          <stop offset="1" stop-color="#e6e6e6"/>
        </radialGradient>
        <radialGradient id="core-glow" cx="285" cy="297" r="70" gradientUnits="userSpaceOnUse">
          <stop offset="0" stop-color="#ffffff" stop-opacity="1"/>
          <stop offset=".5" stop-color="#ffffff" stop-opacity=".7"/>
          <stop offset="1" stop-color="#ffffff" stop-opacity="0"/>
        </radialGradient>
        <linearGradient id="band-yellow" x1="0" y1="0" x2="1" y2="0">
          <stop offset="0" stop-color="#ffd21a" stop-opacity=".15"/>
          <stop offset=".6" stop-color="#ffd21a" stop-opacity=".9"/>
          <stop offset="1" stop-color="#ffd21a"/>
        </linearGradient>
        <linearGradient id="band-purple" x1="0" y1="0" x2="1" y2="0">
          <stop offset="0" stop-color="#d23cf0"/>
          <stop offset=".7" stop-color="#d23cf0" stop-opacity=".7"/>
          <stop offset="1" stop-color="#d23cf0" stop-opacity=".15"/>
        </linearGradient>
        <linearGradient id="band-blue" x1="0" y1="0" x2="1" y2="0">
          <stop offset="0" stop-color="#3d8cff" stop-opacity=".1"/>
          <stop offset=".5" stop-color="#3d8cff" stop-opacity=".55"/>
          <stop offset="1" stop-color="#3d8cff" stop-opacity=".1"/>
        </linearGradient>
      </defs>

      <rect class="backdrop" width="568" height="472" fill="url(#burst)"/>

      <g class="headline">
        <text class="title-what" x="60" y="82" transform="skewX(-6) translate(9 0)">What</text>
        <text class="title-happens" x="280" y="88" textLength="230" lengthAdjust="spacingAndGlyphs">HAPPENS</text>
        <text class="title-intersection" x="60" y="150" fill="url(#title-fill)" textLength="452" lengthAdjust="spacingAndGlyphs">AT THE INTERSECTION?</text>
        <line x1="55" y1="160" x2="515" y2="160" stroke="var(--rule)" stroke-width="1"/>
        <line x1="110" y1="163" x2="460" y2="163" stroke="var(--rule)" stroke-width=".5"/>
      </g>

      <g class="bands">
        <path d="M5 187 H228 A19 19 0 0 1 228 225 H5 Z" fill="url(#band-yellow)"/>
        <path d="M323 187 H568 V225 H323 Z" fill="url(#band-purple)"/>
        <rect x="5" y="415" width="558" height="37" fill="url(#band-blue)"/>
      </g>

      <g class="venn">
        <circle cx="228" cy="266" r="76" fill="var(--yellow)" opacity=".9"/>
        <circle cx="228" cy="266" r="58" fill="#ffe98a" opacity=".55"/>
        <circle cx="323" cy="264" r="82" fill="var(--purple)" opacity=".8"/>
        <circle cx="323" cy="264" r="64" fill="#e98cff" opacity=".45"/>
        <circle cx="284" cy="367" r="84" fill="var(--blue)" opacity=".85"/>
        <circle cx="284" cy="367" r="66" fill="#8dbcff" opacity=".45"/>
        <circle cx="285" cy="297" r="70" fill="url(#core-glow)"/>
      </g>

      <g class="center-mark">
        <path d="M266 282 Q285 276 304 282 Q304 306 285 318 Q266 306 266 282 Z" fill="#ffffff" stroke="#e2e2e2" stroke-width="1"/>
        <text class="question-mark" x="285" y="305">?</text>
      </g>

      <g class="label label-spirituality tile-yellow">
        <rect x="17" y="198" width="17" height="20"/><text class="tile-letter" x="25.5" y="214">S</text>
        <rect x="36" y="198" width="17" height="20"/><text class="tile-letter" x="44.5" y="214">P</text>
        <rect x="55" y="198" width="17" height="20"/><text class="tile-letter" x="63.5" y="214">I</text>
        <rect x="74" y="198" width="17" height="20"/><text class="tile-letter" x="82.5" y="214">R</text>
        <rect x="93" y="198" width="17" height="20"/><text class="tile-letter" x="101.5" y="214">I</text>
        <rect x="112" y="198" width="17" height="20"/><text class="tile-letter" x="120.5" y="214">T</text>
        <rect x="131" y="198" width="17" height="20"/><text class="tile-letter" x="139.5" y="214">U</text>
        <rect x="150" y="198" width="17" height="20"/><text class="tile-letter" x="158.5" y="214">A</text>
        <rect x="169" y="198" width="17" height="20"/><text class="tile-letter" x="177.5" y="214">L</text>
        <rect x="188" y="198" width="17" height="20"/><text class="tile-letter" x="196.5" y="214">I</text>
        <rect x="207" y="198" width="17" height="20"/><text class="tile-letter" x="215.5" y="214">T</text>
        <rect x="226" y="198" width="17" height="20"/><text class="tile-letter" x="234.5" y="214">Y</text>
      </g>

      <g class="label label-sexuality tile-purple">
        <rect x="367" y="198" width="19" height="20"/><text class="tile-letter" x="376.5" y="214">S</text>
        <rect x="388" y="198" width="19" height="20"/><text class="tile-letter" x="397.5" y="214">E</text>
        <rect x="409" y="198" width="19" height="20"/><text class="tile-letter" x="418.5" y="214">X</text>
        <rect x="430" y="198" width="19" height="20"/><text class="tile-letter" x="439.5" y="214">U</text>
        <rect x="451" y="198" width="19" height="20"/><text class="tile-letter" x="460.5" y="214">A</text>
        <rect x="472" y="198" width="19" height="20"/><text class="tile-letter" x="481.5" y="214">L</text>
        <rect x="493" y="198" width="19" height="20"/><text class="tile-letter" x="502.5" y="214">I</text>
        <rect x="514" y="198" width="19" height="20"/><text class="tile-letter" x="523.5" y="214">T</text>
        <rect x="535" y="198" width="19" height="20"/><text class="tile-letter" x="544.5" y="214">Y</text>
      </g>

      <g class="label label-social-justice tile-blue">
        <rect x="138" y="424" width="19" height="21"/><text class="tile-letter" x="147.5" y="441">S</text>
        <rect x="159" y="424" width="19" height="21"/><text class="tile-letter" x="168.5" y="441">O</text>
        <rect x="180" y="424" width="19" height="21"/><text class="tile-letter" x="189.5" y="441">C</text>
        <rect x="201" y="424" width="19" height="21"/><text class="tile-letter" x="210.5" y="441">I</text>
        <rect x="222" y="424" width="19" height="21"/><text class="tile-letter" x="231.5" y="441">A</text>
        <rect x="243" y="424" width="19" height="21"/><text class="tile-letter" x="252.5" y="441">L</text>
        <rect x="277" y="424" width="19" height="21"/><text class="tile-letter" x="286.5" y="441">J</text>
        <rect x="298" y="424" width="19" height="21"/><text class="tile-letter" x="307.5" y="441">U</text>
        <rect x="319" y="424" width="19" height="21"/><text class="tile-letter" x="328.5" y="441">S</text>
        <rect x="340" y="424" width="19" height="21"/><text class="tile-letter" x="349.5" y="441">T</text>
        <rect x="361" y="424" width="19" height="21"/><text class="tile-letter" x="370.5" y="441">I</text>
        <rect x="382" y="424" width="19" height="21"/><text class="tile-letter" x="391.5" y="441">C</text>
        <rect x="403" y="424" width="19" height="21"/><text class="tile-letter" x="412.5" y="441">E</text>
      </g>
    </svg>
  </section>
</main>
</body>
</html>
```